Business Card design for Property Developer

We need a business card design for a Melbourne based Property Developer called "Kestrelmoor Holdings Pty Ltd".

We subdivide land and onsell to builders etc.

We already have a company logo, which is attached. Also I have attached the layout requirements from the printer. We would like a 2-sided design with one side displaying our logo by itself and the other with the required info, such as name, address, tel no., email, abn etc. The card will need to be used by 4 members of staff so name and contact details should be interchangable.
Updates

If possible, can you please write "name' "job position" "phone" "email" "address" on the card but leave them so I can add the details at a later time. Thank you. Also I plan on printing with UV spot printing as a background on the card. Keep this is mind when designing.

Thanks again.

Hello designers, please do not include pics of houses, house plansĀ or construction machinery etc as we really do not like the way it looks. Thank you.

Target Market(s)

Real Estate Agents, Land Owners, Local Council Departments, Govt Bodies, other Developers etc.

Industry/Entity Type

Business

Requirements
Must have
• 2-sided design with one side displaying our logo by itself and the other with the required info, such as name, address, tel no., email, abn etc.

```html
<!DOCTYPE html>
<html lang="en">
<head>
<meta charset="utf-8">
<title>Kestrelmoor Holdings – Business Card</title>
<link href="https://fonts.googleapis.com/css2?family=Arimo:wght@400;700&display=swap" rel="stylesheet">
<style>
  :root {
    --page-white: #ffffff;
    --board-grey: #58585a;
    --card-white: #ffffff;
    --brand-blue: #1f66b8;
    --brand-blue-light: #3fa2e4;
    --brand-blue-deep: #123f86;
    --ink: #2b2b2b;
    --job-blue: #2357a6;
  }
  * { margin: 0; padding: 0; box-sizing: border-box; }
  html, body {
    width: 1200px; height: 502px; overflow: hidden;
    background: var(--page-white);
    font-family: "Arimo", Arial, sans-serif;
  }
  .board {
    position: absolute; left: 0; top: 74px;
    width: 1140px; height: 428px;
    background: var(--board-grey);
  }
  .card {
    position: absolute; top: 124px;
    width: 480px; height: 270px;
    background: var(--card-white);
    overflow: hidden;
  }
  .card--front { left: 94px; }
  .card--back { left: 586px; width: 478px; }
  .card__accent {
    position: absolute; top: 0; left: 0;
    width: 100%; height: 100%;
  }
  .brand {
    position: absolute; text-align: center;
    color: var(--brand-blue); font-weight: 700;
  }
  .brand__dot {
    display: block; margin: 0 auto;
    border-radius: 50%;
    background: var(--brand-blue);
  }
  .brand--front { left: 250px; top: 126px; width: 220px; }
  .brand--front .brand__dot { width: 68px; height: 68px; margin-bottom: 12px; }
  .brand--front .brand__name { font-size: 15px; letter-spacing: 0.3px; }
  .brand--back { left: 24px; top: 46px; width: 100px; }
  .brand--back .brand__dot { width: 28px; height: 28px; margin-bottom: 4px; }
  .brand--back .brand__name { font-size: 8px; }
  .contact {
    position: absolute; left: 36px; top: 108px;
    color: var(--ink);
  }
  .contact__name { font-size: 18px; line-height: 20px; }
  .contact__role { font-size: 13px; line-height: 18px; color: var(--job-blue); }
  .contact__details { margin-top: 26px; list-style: none; font-size: 13px; line-height: 18px; }
</style>
</head>
<body>
  <div class="board"></div>

  <section class="card card--front" aria-label="Card front">
    <svg class="card__accent" viewBox="0 0 480 270" aria-hidden="true">
      <defs>
        <linearGradient id="accentFront" x1="0" y1="0" x2="1" y2="1">
          <stop offset="0" stop-color="var(--brand-blue-light)"/>
          <stop offset="1" stop-color="var(--brand-blue-deep)"/>
        </linearGradient>
      </defs>
      <ellipse cx="110" cy="188" rx="80" ry="12" fill="#000" opacity="0.12"/>
      <circle cx="96" cy="76" r="110" fill="url(#accentFront)"/>
    </svg>
    <div class="brand brand--front">
      <span class="brand__dot"></span>
      <span class="brand__name">Kestrelmoor Holdings</span>
    </div>
  </section>

  <section class="card card--back" aria-label="Card back">
    <svg class="card__accent" viewBox="0 0 478 270" aria-hidden="true">
      <defs>
        <linearGradient id="accentBack" x1="0" y1="0" x2="1" y2="1">
          <stop offset="0" stop-color="var(--brand-blue-light)"/>
          <stop offset="1" stop-color="var(--brand-blue-deep)"/>
        </linearGradient>
      </defs>
      <ellipse cx="450" cy="184" rx="70" ry="12" fill="#000" opacity="0.12"/>
      <circle cx="454" cy="76" r="110" fill="url(#accentBack)"/>
    </svg>
    <div class="brand brand--back">
      <span class="brand__dot"></span>
      <span class="brand__name">Kestrelmoor Holdings</span>
    </div>
    <div class="contact">
      <p class="contact__name">name</p>
      <p class="contact__role">job position</p>
      <ul class="contact__details">
        <li>phone</li>
        <li>email</li>
        <li>address</li>
      </ul>
    </div>
  </section>
</body>
</html>
```